Business Card Design Project

I require a business card with the following information on them for various different people;
name
m:
f:
e:
I have a logo already and will attached that. We are in the construction industry. I require something clean and simple but eye catching at the same time. You can use another colour with our logo if you like and you can style the logo as well if you wish. I am open.
Also it needs to be front and back design.
Industry/Entity Type
Construction
Requirements
Must have
- Logo, name, mobile, fax and email address.
Front and back design

```html
<!DOCTYPE html>
<html lang="en">
<head>
<meta charset="utf-8">
<title>Stonebridge Developments – Business Cards</title>
<link rel="stylesheet" href="https://fonts.googleapis.com/css2?family=Lato:wght@400;700&display=swap">
<style>
  :root {
    --bg: #ecebe8;
    --card: #ffffff;
    --green: #58b044;
    --green-light: #c2dc5c;
    --green-mid: #8cc63f;
    --charcoal: #3a3b3d;
    --charcoal-dark: #2b2c2e;
    --ink: #333333;
    --grey: #666666;
  }
  * { box-sizing: border-box; margin: 0; padding: 0; }
  html, body { width: 1200px; height: 757px; overflow: hidden; }
  body {
    background: var(--bg);
    font-family: "Lato", sans-serif;
    position: relative;
  }
  .card {
    position: absolute;
    width: 513px;
    height: 292px;
    border-radius: 14px;
    overflow: hidden;
    background: var(--card);
    box-shadow: 0 1px 3px rgba(0,0,0,.25);
  }
  .card--front { left: 85px; top: 228px; }
  .card--back-green {
    left: 654px; top: 65px;
    background: radial-gradient(ellipse at 58% 35%, var(--green-light) 0%, var(--green-mid) 35%, var(--green) 75%);
    display: flex; align-items: center; justify-content: center;
  }
  .card--back-white {
    left: 651px; top: 382px;
    display: flex; align-items: center; justify-content: center;
  }
  .brand {
    display: flex; align-items: center; gap: 10px;
    color: var(--green);
    font-weight: 400;
    font-size: 30px;
    letter-spacing: .5px;
    white-space: nowrap;
  }
  .brand__square {
    width: 28px; height: 28px;
    background: var(--green);
    border-radius: 3px;
  }
  .card--front .brand {
    position: absolute; top: 50px; left: 50%; transform: translateX(-50%);
  }
  .card--back-green .brand { color: #ffffff; font-size: 38px; }
  .card--back-green .brand__square { background: #ffffff; width: 36px; height: 36px; }
  .contact {
    position: absolute; top: 152px; left: 0; width: 100%;
    text-align: center; color: var(--ink); font-size: 12.5px; line-height: 25px;
  }
  .contact__row { display: flex; justify-content: center; gap: 10px; }
  .contact__item { display: inline-flex; align-items: center; gap: 5px; }
  .contact__icon { width: 10px; height: 10px; fill: var(--ink); }
  .footer-band { position: absolute; left: 0; bottom: 0; width: 100%; height: 46px; }
  .holder {
    position: absolute; right: 62px; bottom: 12px;
    color: var(--green); font-weight: 700; font-size: 15.5px;
  }
</style>
</head>
<body>

  <section class="card card--front">
    <div class="brand"><span class="brand__square"></span>Stonebridge Developments</div>

    <div class="contact">
      <div class="contact__row">
        <span class="contact__item">
          <svg class="contact__icon" viewBox="0 0 10 10"><rect x="2.5" y="0" width="5" height="10" rx="1"/><rect x="3.5" y="1.5" width="3" height="4" fill="#fff"/></svg>
          +91 98765 43210
        </span>
        <span class="contact__item">
          <svg class="contact__icon" viewBox="0 0 10 10"><rect x="2.5" y="0.5" width="5" height="3"/><rect x="0.5" y="3.5" width="9" height="5" rx="1"/></svg>
          +91 98765 43210
        </span>
      </div>
      <div class="contact__row">
        <span class="contact__item">
          <svg class="contact__icon" viewBox="0 0 10 10"><rect x="0.5" y="2" width="9" height="6"/><path d="M0.5 2 L5 5.5 L9.5 2" stroke="#fff" fill="none" stroke-width="1"/></svg>
          hello@stonebridgebuild.com
        </span>
      </div>
    </div>

    <svg class="footer-band" viewBox="0 0 513 46" preserveAspectRatio="none">
      <defs>
        <linearGradient id="greenStrip" x1="0" x2="1" y1="0" y2="0">
          <stop offset="0" stop-color="#58b044"/>
          <stop offset="1" stop-color="#c2dc5c"/>
        </linearGradient>
        <linearGradient id="darkBand" x1="0" x2="0" y1="0" y2="1">
          <stop offset="0" stop-color="#4a4b4d"/>
          <stop offset="1" stop-color="#2b2c2e"/>
        </linearGradient>
      </defs>
      <polygon points="0,3 266,3 256,16 0,16" fill="url(#greenStrip)"/>
      <polygon points="274,0 513,0 513,46 0,46 0,26 254,26" fill="url(#darkBand)"/>
    </svg>
    <div class="holder">Your Name , Title</div>
  </section>

  <section class="card card--back-green">
    <div class="brand"><span class="brand__square"></span>Stonebridge</div>
  </section>

  <section class="card card--back-white">
    <div class="brand"><span class="brand__square"></span>Stonebridge Developments</div>
  </section>

</body>
</html>
```